Tooth Fairy Certificates with a Brown Tooth Fairy character on it (animation)
Tooth Certificate
I needs a name and date slot
also boxes for checks or stars next to each word
- clean
- shiny
- needs more brushing

Great Job, I'm so Proud of you! keep up the great brushing!

I need 4 per 11x8 page or 2- 5' 7 per page.

```html
<!DOCTYPE html>
<html lang="en">
<head>
<meta charset="UTF-8">
<title>Tooth Fairy Certificate</title>
<link href="https://fonts.googleapis.com/css2?family=Fredoka:wght@600&family=Poppins:wght@400;500;700&family=Tinos&family=Damion&display=swap" rel="stylesheet">
<style>
  :root {
    --sky: #dbe9f0;
    --card: #ffffff;
    --ink: #3d6a96;
    --sun: #fbf68a;
    --badge-dot: #7f8fd8;
    --box-line: #6a7f93;
    --tooth-light: #eef3f7;
    --tooth-shade: #c9d6e2;
    --kid-hair: #f7e46a;
    --kid-lilac: #d9c8ee;
  }
  * { margin: 0; padding: 0; box-sizing: border-box; }
  html, body { width: 857px; height: 1200px; overflow: hidden; background: var(--sky); }
  .certificate { position: relative; width: 857px; height: 1200px; background: var(--sky); color: var(--ink); }
  .card {
    position: absolute; left: 100px; top: 152px; width: 667px; height: 865px;
    background: var(--card); border-radius: 17px;
    box-shadow: 0 10px 14px -6px rgba(60, 80, 100, 0.35);
  }
  .badge { position: absolute; left: 352px; top: 76px; width: 152px; height: 152px; }
  .title {
    position: absolute; left: 100px; width: 667px; top: 283px; text-align: center;
    font-family: "Fredoka", sans-serif; font-weight: 600; font-size: 41px; line-height: 50px;
  }
  .frame { position: absolute; left: 170px; top: 335px; width: 530px; height: 527px; }
  .line { position: absolute; left: 170px; width: 530px; text-align: center; font-family: "Poppins", sans-serif; }
  .award-label { top: 375px; font-size: 25px; }
  .recipient { top: 433px; font-size: 42px; font-weight: 700; }
  .occasion { top: 523px; font-size: 27px; }
  .date { top: 574px; font-size: 26px; font-weight: 700; }
  .checklist { position: absolute; left: 215px; top: 670px; list-style: none; font-family: "Tinos", serif; font-size: 32px; }
  .checklist li { display: flex; align-items: center; height: 48px; }
  .checkbox {
    width: 33px; height: 33px; border: 1.5px solid var(--box-line); border-radius: 4px;
    margin-right: 9px; background: var(--card);
  }
  .tooth-art { position: absolute; border-radius: 40% 40% 35% 35%; background: linear-gradient(160deg, var(--tooth-light), var(--tooth-shade)); }
  .tooth-right { left: 702px; top: 486px; width: 93px; height: 106px; }
  .tooth-left { left: 90px; top: 805px; width: 86px; height: 119px; }
  .kid-art {
    position: absolute; left: 524px; top: 852px; width: 328px; height: 329px; border-radius: 30px;
    background: linear-gradient(180deg, var(--kid-hair) 0%, #fbeec0 40%, var(--kid-lilac) 100%);
  }
  .cheer {
    position: absolute; left: 0; width: 534px; top: 944px; text-align: center;
    font-family: "Damion", cursive; font-size: 38px; line-height: 78px;
  }
</style>
</head>
<body>
<main class="certificate">
  <div class="card"></div>

  <svg class="badge" viewBox="-80 -80 160 160" aria-hidden="true">
    <g fill="var(--sun)">
      <circle r="64"/>
      <circle cx="62" cy="0" r="15"/><circle cx="53.7" cy="31" r="15"/><circle cx="31" cy="53.7" r="15"/>
      <circle cx="0" cy="62" r="15"/><circle cx="-31" cy="53.7" r="15"/><circle cx="-53.7" cy="31" r="15"/>
      <circle cx="-62" cy="0" r="15"/><circle cx="-53.7" cy="-31" r="15"/><circle cx="-31" cy="-53.7" r="15"/>
      <circle cx="0" cy="-62" r="15"/><circle cx="31" cy="-53.7" r="15"/><circle cx="53.7" cy="-31" r="15"/>
    </g>
    <circle r="34" fill="var(--badge-dot)"/>
  </svg>

  <h1 class="title">Tooth Fairy Certificate</h1>

  <svg class="frame" viewBox="0 0 530 527" aria-hidden="true">
    <polygon points="100,5.5 430,5.5 524.5,100 524.5,427 430,521.5 100,521.5 5.5,427 5.5,100"
             fill="none" stroke="var(--sun)" stroke-width="11"/>
  </svg>

  <p class="line award-label">Award To :</p>
  <p class="line recipient">name</p>
  <p class="line occasion">Who lost him first tooth</p>
  <p class="line date">January 01, 2023</p>

  <ul class="checklist">
    <li><span class="checkbox"></span>Clean</li>
    <li><span class="checkbox"></span>Shiny</li>
    <li><span class="checkbox"></span>Needs more brushing</li>
  </ul>

  <div class="tooth-art tooth-right" role="img" aria-label="Sketched tooth illustration with sparkles"></div>
  <div class="tooth-art tooth-left" role="img" aria-label="Sketched tooth illustration with sparkles"></div>
  <div class="kid-art" role="img" aria-label="Illustration of a child with pigtails brushing teeth"></div>

  <p class="cheer">Great Job. I'm so Proud of<br>you! keep up the great<br>brushing!</p>
</main>
</body>
</html>
```